New design and logo for www.plxmodels.com

Hi, we need a new design for the site www.plxmodels.com
It's a scale modelling e-commerce website (no RC models or die cast models, only static models to build) which is a highly technical hobby (exact scale reproduction from passionated starting with the kit we sell using different material (paint, airbrush...)). Main fields are military aircrafts, military vehicles and scale figures. They are also less important fields like reference books, boats, civilian vehicles, tools like aibrushes, paints and so on.
Every scale model come with plans for mounting the items (mainly on plastic sprues), instructions for painting and most of them have decals to apply.
We don't want a military feeling, and visitors must understand immediately that our site is not about RC models or die cast models but are kits to build. They are not toys, customers are mainly adults aroud 30-50 (hobby starting aroud 14 years old), mainly mens but a few girls are in the hobby too (mainly in figures).
We would like to get rid of the right banner and have a search engine (actually on left top of the menu) and menu (actually on left) on all the pages. We need the main page banners for new products or announcements and the first page must show the last added product.
The product's list (click on any link on left) must be improved and the product's detail too.
Here are the page sample to make template for (same design but we need to know how to build them):
Main page: http://www.plxmodels.com/
Product's list: http://www.plxmodels.com/planes-1_48-aircraft-kits-c-21_27.html
Product's detail: http://www.plxmodels.com/korvane-kv41207-1_48-brandtner-bx-204d-wespe-foreign-af-p-30059.html
Those items must be visible at any time (design can be changed without problem) :
The cart with content once you add something on it
The language seletor
The currency selector
Chatterly Like link
link to account
newsletter register form (actually not visible on our site, only a field for entering the email but should be appealing)
You are free to put all other informations (contact, general informations, payments...) where you want
Design must be done in a way it will improve the sales and feel confident with the site. We have no preferences for colors and disposition, new logo proposal is also highly welcome (with eventually an extra fee, but we won't start 2 projects).
If you have any question, please feel free to contact us.
Thank you for reading, do your best and good luck!
Target Market(s)
Mainly mens 30-50
Industry/Entity Type
E-Commerce
Requirements
Must have
- Understand it's a scale modeling site and not toy, die cast or RC
The language seletor
The currency selector
Chatterly Like link
link to account
Nice to have
- New logo

```html
<!DOCTYPE html>
<html lang="en">
<head>
<meta charset="utf-8">
<title>PLXmodels.com – Scale model kits</title>
<link rel="stylesheet" href="https://fonts.googleapis.com/css2?family=Cabin:wght@400;600&family=Tinos:wght@400;700&display=swap">
<style>
:root{
  --page:#f2f2f2;
  --sheet:#ffffff;
  --brand-blue:#2f6aa8;
  --teal:#1b9ab2;
  --rust:#b4500f;
  --headline:#c0392b;
  --ink:#222;
  --muted:#6b6b6b;
  --line:#9a9a9a;
  --btn-blue:#3d86d6;
}
*{box-sizing:border-box;margin:0;padding:0}
html,body{width:1097px;height:1200px;overflow:hidden;background:var(--page)}
body{position:relative;font-family:"Tinos",serif;color:var(--ink)}
.abs{position:absolute}
.sheet{left:62px;top:0;width:969px;height:1058px;background:var(--sheet);box-shadow:0 2px 4px rgba(0,0,0,.35)}
.logo{left:74px;top:16px;font-family:"Tinos",serif;font-weight:700;font-size:34px;color:var(--brand-blue);display:flex;align-items:center;gap:8px}
.logo .dot{width:14px;height:14px;background:var(--brand-blue)}
.flags{left:575px;top:11px;display:flex;gap:4px}
.flag{width:22px;height:14px;border:1px solid #999}
.currency{left:723px;top:8px;width:148px;height:19px;border:1px solid #bbb;border-radius:9px;font-size:11px;padding:2px 10px;display:flex;justify-content:space-between;align-items:center;background:#fafafa}
.social{left:915px;top:10px;display:flex;gap:4px;font-size:10px;font-family:"Cabin",sans-serif}
.social span{border:1px solid #c5cde0;background:#eef1f8;color:#3b5998;padding:1px 4px;border-radius:2px}
.account{left:788px;top:53px;font-size:15px;display:flex;gap:15px}
.cart{left:916px;top:52px;width:114px;height:22px;background:var(--teal);color:#fff;font-size:14px;text-align:center;line-height:22px}
.promo{left:68px;top:75px;width:449px;height:202px;border:1px solid #ccc;box-shadow:0 2px 3px rgba(0,0,0,.35);background:#f9f9f9;text-align:center;font-family:"Cabin",sans-serif}
.promo h1{font-weight:400;color:var(--headline);font-size:26px;line-height:26px;margin-top:24px}
.promo .sub{color:#666;font-size:17px;margin-top:10px}
.promo .small{color:#666;font-size:15px;line-height:15px;margin-top:6px}
.promo .btn{display:inline-block;margin-top:15px;width:148px;height:31px;border-radius:5px;background:var(--btn-blue);color:#fff;font-size:15px;line-height:31px}
.banner{left:517px;top:95px;width:510px;height:162px;border:1px solid #999;background:#fff}
.banner .art{position:absolute;left:1px;top:11px;width:503px;height:138px;background:linear-gradient(90deg,#8e2f25,#30527a 55%,#b52d2b)}
.panel{left:68px;width:233px;border:1px solid #aaa}
.search{top:304px;height:175px;background:var(--teal);padding:12px 9px}
.field{height:21px;border-radius:10px;background:#fff;border:1px solid #ccc;font-size:14px;padding-left:9px;line-height:19px;margin-bottom:13px;display:flex;justify-content:space-between}
.field .arr{width:33px;background:#4a4a4a;border-radius:0 10px 10px 0;color:#fff;text-align:center;font-size:10px}
.search .go{display:block;margin:-3px auto 0;width:111px;height:22px;border-radius:8px;background:#000;color:#fff;text-align:center;font-size:14px;line-height:22px}
.search .adv{text-align:center;color:#111;font-size:16px;margin-top:6px}
.panel-head{background:var(--rust);color:#fff;font-size:19px;height:32px;line-height:32px;padding-left:11px}
.news{top:504px;height:117px;background:#f6f6f6}
.news .email{margin:18px auto 0;width:193px;height:22px;border:1px solid #ccc;background:#fff;color:#777;font-size:15px;padding-left:13px;line-height:20px}
.news .sub-btn{margin:10px auto 0;width:136px;height:24px;background:#1a1a1a;color:#fff;text-align:center;font-size:16px;line-height:24px}
.cats{top:646px;height:374px;background:#f4f4f4}
.cats .group{margin:0 22px 0 28px;border-bottom:1px dashed #555;padding:10px 0 10px}
.cats .group:last-child{border:0}
.cats h3{font-weight:400;font-size:17px}
.cats ul{list-style:none;margin-left:20px;font-size:13px;color:var(--muted);line-height:15.5px;margin-top:2px}
.cats li::before{content:"";display:inline-block;width:4px;height:4px;background:var(--rust);margin-right:9px;vertical-align:middle}
.title{left:368px;top:293px;font-family:"Cabin",sans-serif;font-weight:600;font-size:27px;color:var(--rust)}
.card{width:214px;height:215px;border:1px solid #777;background:#fff}
.card .img{position:absolute;left:26px;top:36px;width:162px;height:100px}
.card .name{position:absolute;left:29px;top:151px;font-size:13px;line-height:12px}
.card .price{position:absolute;left:32px;top:189px;font-size:11px;font-weight:700}
.card .buy{position:absolute;left:128px;top:187px;width:61px;height:15px;background:var(--teal);border:1px solid #333;color:#fff;font-size:11px;text-align:center;line-height:13px}
.foot-links{left:69px;top:1092px;font-size:14px;line-height:22px}
.foot-links .row{display:flex;gap:31px}
.pay-label{left:741px;top:1085px;font-size:11px}
.pay{left:744px;top:1103px;display:flex;gap:5px}
.pay span{width:44px;height:28px;border:1px solid #ccc;font-family:"Cabin",sans-serif;font-size:9px;display:flex;align-items:center;justify-content:center;background:#fff;color:#333}
.pay .bank{background:#1e4f8c;color:#fff;font-size:12px}
.copy{left:0;width:1097px;top:1157px;text-align:center;font-size:9.5px}
</style>
</head>
<body>
<div class="abs sheet"></div>

<div class="abs logo"><span class="dot"></span>PLXmodels.com</div>
<div class="abs flags">
  <svg class="flag" viewBox="0 0 22 14"><rect width="22" height="14" fill="#1f3f8a"/><path d="M0 0L22 14M22 0L0 14" stroke="#fff" stroke-width="3"/><path d="M11 0V14M0 7H22" stroke="#fff" stroke-width="4"/><path d="M11 0V14M0 7H22" stroke="#c8102e" stroke-width="2"/></svg>
  <svg class="flag" viewBox="0 0 3 2"><rect width="1" height="2" fill="#009246"/><rect x="1" width="1" height="2" fill="#fff"/><rect x="2" width="1" height="2" fill="#ce2b37"/></svg>
  <svg class="flag" viewBox="0 0 3 2"><rect width="1" height="2" fill="#0055a4"/><rect x="1" width="1" height="2" fill="#fff"/><rect x="2" width="1" height="2" fill="#ef4135"/></svg>
  <svg class="flag" viewBox="0 0 3 3"><rect width="3" height="1" fill="#000"/><rect y="1" width="3" height="1" fill="#dd0000"/><rect y="2" width="3" height="1" fill="#ffce00"/></svg>
</div>
<div class="abs currency">Select Currency <svg width="12" height="9" viewBox="0 0 12 9"><path d="M0 0H12L6 9Z" fill="#111"/></svg></div>
<div class="abs social"><span>Chatterly Like</span><span>2</span><span>Send</span></div>
<div class="abs account"><span>Register</span><span>Login</span></div>
<div class="abs cart">My cart: 0 items</div>

<div class="abs promo">
  <h1>The Best online shop for<br>model kits and detail sets.</h1>
  <p class="sub">Permanent low prices 10% to 50% less</p>
  <p class="small">A big choice of model kits, figures,<br>detail kits, tools and much more</p>
  <span class="btn">Know More</span>
</div>
<div class="abs banner"><div class="art" role="img" aria-label="Banner: Vortan 1/35 VK-9 battle tank kit box art – It's here!"></div></div>

<div class="abs panel search">
  <div class="field">Keywords</div>
  <div class="field">Categories <span class="arr">▼</span></div>
  <div class="field">Manufacturers <span class="arr">▼</span></div>
  <span class="go">Search</span>
  <p class="adv">Advanced Search</p>
</div>

<div class="abs panel news">
  <div class="panel-head">Newsletter</div>
  <div class="email">Enter your email</div>
  <div class="sub-btn">Subscribe</div>
</div>

<div class="abs panel cats">
  <div class="panel-head">Categories</div>
  <div class="group"><h3>Destocking</h3><ul><li>1/35 AFV upgrade kits</li></ul></div>
  <div class="group"><h3>Planes</h3><ul>
    <li>1/35 AFV upgrade kits</li><li>1/144 Aircraft Decals</li><li>1/144 Aircraft Kits</li><li>1/144 Aircraft upgrade kit</li><li>1/200 Aircraft Kits</li><li>1/24 Aircraft Decals</li><li>1/24 Aircraft Kits</li><li>1/24 Aircraft upgrade kits</li><li>1/32 Aircraft Decals</li><li>1/32 Aircraft Kits</li></ul></div>
  <div class="group"><h3>AFVs</h3></div>
  <div class="group"><h3>Figurines</h3></div>
</div>

<div class="abs title">New Products :</div>

<div class="abs card" style="left:364px;top:341px"><div class="img" role="img" aria-label="Airliner decal sheet" style="background:linear-gradient(#dfe8f2,#b9cfe3)"></div><p class="name">1/144 Corvane 880 Meridian<br>Pacific,silk-screened decals</p><span class="price">CHF 38.20</span><span class="buy">Buy Now</span></div>
<div class="abs card" style="left:587px;top:341px"><div class="img" role="img" aria-label="Resin landing gear parts" style="background:#6cc0de"></div><p class="name">1/144 Corvane 880 Meridian<br>Pacific,silk-screened decals</p><span class="price">CHF 38.20</span><span class="buy">Buy Now</span></div>
<div class="abs card" style="left:808px;top:341px"><div class="img" role="img" aria-label="Metal barrel parts" style="background:#b8d31e"></div><p class="name">1/144 Corvane 880 Meridian<br>Pacific,silk-screened decals</p><span class="price">CHF 38.20</span><span class="buy">Buy Now</span></div>

<div class="abs card" style="left:364px;top:566px"><div class="img" role="img" aria-label="Bomber aircraft box art" style="background:linear-gradient(#7a8a8a,#c9d2cf)"></div><p class="name">1/144 Corvane 880 Meridian<br>Pacific,silk-screened decals</p><span class="price">CHF 38.20</span><span class="buy">Buy Now</span></div>
<div class="abs card" style="left:587px;top:566px"><div class="img" role="img" aria-label="Helicopter box art" style="background:linear-gradient(#3b6fb0,#8aaed8)"></div><p class="name">1/144 Corvane 880 Meridian<br>Pacific,silk-screened decals</p><span class="price">CHF 38.20</span><span class="buy">Buy Now</span></div>
<div class="abs card" style="left:808px;top:566px"><div class="img" role="img" aria-label="Biplane trainer box art" style="background:linear-gradient(#d9d2c4,#9bb7d8)"></div><p class="name">1/144 Corvane 880 Meridian<br>Pacific,silk-screened decals</p><span class="price">CHF 38.20</span><span class="buy">Buy Now</span></div>

<div class="abs card" style="left:364px;top:793px"><div class="img" role="img" aria-label="Airliner decal sheet" style="background:linear-gradient(#dfe8f2,#b9cfe3)"></div><p class="name">1/144 Corvane 880 Meridian<br>Pacific,silk-screened decals</p><span class="price">CHF 38.20</span><span class="buy">Buy Now</span></div>
<div class="abs card" style="left:587px;top:793px"><div class="img" role="img" aria-label="Resin landing gear parts" style="background:#6cc0de"></div><p class="name">1/144 Corvane 880 Meridian<br>Pacific,silk-screened decals</p><span class="price">CHF 38.20</span><span class="buy">Buy Now</span></div>
<div class="abs card" style="left:808px;top:793px"><div class="img" role="img" aria-label="Metal barrel parts" style="background:#b8d31e"></div><p class="name">1/144 Corvane 880 Meridian<br>Pacific,silk-screened decals</p><span class="price">CHF 38.20</span><span class="buy">Buy Now</span></div>

<div class="abs foot-links">
  <div class="row"><span>Home</span><span>Pre-Order</span><span>Sales</span><span>FAQ</span><span>Contact</span></div>
  <div>Terms and conditions of use</div>
</div>
<div class="abs pay-label">We accept payments from:</div>
<div class="abs pay"><span class="bank">BANK</span><span>Findex</span><span>PayLoop</span><span>Westline</span><span>Cardmark</span><span>Vista</span></div>
<div class="abs copy">All rights reserved to PLXmodels.Copyrights@2013</div>
</body>
</html>
```